Flyer for the Radiant Harvest Worship Day 2020

I am looking to create a flyer for a one day prayer retreat our church is organizing.
This flyer will be posted on social media, websites and will also be printed so it can be mailed to people.
I am looking for something professional, with good use of our logo and band colors (logo colors).
I am counting on the designer's skill, creativity, art and knowledge of media communication to produce a flyer that will effectively and quickly convey the message we are trying to spread.
CONTENT OF THE FLYER:
Event title: Radiant Harvest Worship Day
Date: Tuesday July 2nd, 2020
Time: 11:00AM - 7:00PM
Belmora Hotel, 4876 Willowmere Street, Portland, Maine 04987 (Room: Evergrove)
Event Key words to highlight what the event is about: Prayer, Sharing the Word, Panel discussion, prophecy, Impartation.
Key phrases:
A one day prayer retreat.
Jesus Chris is Lord
Contact info:
www.toluvek.org
Phone: 207 555 0183
Email: contact@brightmeadowfold.org

```html
<!DOCTYPE html>
<html lang="en">
<head>
<meta charset="utf-8">
<title>Radiant Harvest Worship Day 2020</title>
<link rel="stylesheet" href="https://fonts.googleapis.com/css2?family=Arimo:wght@400;700&family=Cinzel:wght@400;600&family=Pinyon+Script&display=swap">
<style>
  :root {
    --page: #ffffff;
    --ink-dark: #140a06;
    --ember: #c8641c;
    --amber: #e9a23a;
    --gold: #d99a2b;
    --sky: #f2c25a;
    --white: #ffffff;
  }
  * { box-sizing: border-box; margin: 0; padding: 0; }
  html, body { width: 1200px; height: 1200px; overflow: hidden; background: var(--page); }
  .flyer {
    position: absolute; left: 202px; top: 86px; width: 797px; height: 1027px;
    background: var(--ink-dark); overflow: hidden; color: var(--white);
    font-family: "Arimo", Arial, sans-serif;
  }
  .hero-photo {
    position: absolute; left: 0; top: 0; width: 100%; height: 760px;
    background:
      radial-gradient(ellipse 40% 22% at 50% 62%, rgba(240,150,70,.55), transparent 70%),
      linear-gradient(180deg, var(--sky) 0%, var(--amber) 14%, var(--ember) 38%, #8a3a14 58%, #b2531e 70%, #4a1c0c 86%, var(--ink-dark) 100%);
  }
  .brand {
    position: absolute; top: 70px; left: 0; width: 100%; text-align: center;
    font-family: "Arimo", Arial, sans-serif; font-weight: 700;
    font-size: 34px; letter-spacing: 4px; color: var(--white);
  }
  .title { position: absolute; left: 0; width: 100%; text-align: center; font-weight: 700; line-height: 1; }
  .title-top { top: 142px; font-size: 70px; }
  .title-main { top: 208px; font-size: 92px; }
  .tagline { position: absolute; top: 302px; width: 100%; text-align: center; font-size: 30px; }
  .declaration {
    position: absolute; top: 362px; width: 100%; text-align: center;
    font-family: "Pinyon Script", cursive; font-size: 58px; color: var(--gold);
  }
  .details { position: absolute; top: 700px; left: 0; width: 100%; height: 90px; }
  .day-num { position: absolute; left: 72px; top: 4px; font-size: 92px; font-weight: 700; line-height: 1; }
  .month-year { position: absolute; left: 184px; top: 10px; font-size: 36px; font-weight: 700; line-height: 1.05; }
  .divider { position: absolute; top: 6px; width: 2px; height: 80px; background: rgba(255,255,255,.6); }
  .venue { position: absolute; left: 302px; top: 10px; width: 214px; text-align: center; font-size: 15.5px; font-weight: 700; line-height: 1.22; }
  .weekday { position: absolute; left: 528px; top: 8px; width: 200px; text-align: center; font-size: 38px; font-weight: 700; line-height: 1.05; }
  .weekday span { font-size: 33px; }
  .highlights {
    position: absolute; left: 110px; top: 808px; width: 576px; height: 132px;
    border: 2px solid var(--gold);
    display: grid; grid-template-columns: 320px 1fr; align-content: center; row-gap: 9px;
    padding-left: 34px;
    font-family: "Cinzel", serif; font-size: 22px; list-style: none;
  }
  .highlights li::before { content: "\25C6"; font-size: 12px; margin-right: 10px; vertical-align: 3px; }
  .contact {
    position: absolute; top: 970px; left: 0; width: 100%;
    display: flex; justify-content: center; gap: 26px; align-items: center;
    font-family: "Cinzel", serif; font-size: 17px;
  }
  .contact-item { display: flex; align-items: center; gap: 9px; }
  .contact svg { width: 24px; height: 24px; }
</style>
</head>
<body>
<main class="flyer">
  <div class="hero-photo" role="img" aria-label="Warm golden desert scene with an open Bible in the sky and a man kneeling in prayer"></div>
  <div class="brand">TOLUVEK</div>
  <h1 class="title title-top">RADIANT HARVEST</h1>
  <h1 class="title title-main">WORSHIP DAY</h1>
  <p class="tagline">A one day prayer retreat.</p>
  <p class="declaration">Jesus Christ is Lord</p>

  <section class="details">
    <div class="day-num">02</div>
    <div class="month-year">JULY<br>2020</div>
    <div class="divider" style="left:296px"></div>
    <div class="venue">EVERGROVE ROOM<br>Belmora Hotel,<br>4876 Willowmere Street,<br>Portland, Maine 04987</div>
    <div class="divider" style="left:522px"></div>
    <div class="weekday">TUESDAY<br><span>11AM—7PM</span></div>
  </section>

  <ul class="highlights">
    <li>Prayer</li><li>Prophecy</li>
    <li>Sharing the Word</li><li>Impartation</li>
    <li>Panel discussion</li>
  </ul>

  <footer class="contact">
    <div class="contact-item">
      <svg viewBox="0 0 24 24"><circle cx="12" cy="12" r="10.5" fill="none" stroke="#e9a23a" stroke-width="1.8"/><path d="M8.5 7c-.8.8-.9 2.3.4 4.4 1.4 2.3 3 3.9 5 4.9 1.5.7 2.6.4 3.1-.3l-1.9-1.9-1.5.8c-1-.5-2.3-1.8-2.9-3l.8-1.5L9.6 6.6z" fill="#e9a23a"/></svg>
      <span>207 555 0183</span>
    </div>
    <div class="contact-item">
      <svg viewBox="0 0 24 24"><rect x="3" y="6" width="18" height="12" rx="1" fill="#e9a23a"/><path d="M3 6l9 7 9-7" fill="none" stroke="#140a06" stroke-width="1.5"/></svg>
      <span>contact@brightmeadowfold.org</span>
    </div>
    <div class="contact-item">
      <svg viewBox="0 0 24 24" fill="none" stroke="#e9a23a" stroke-width="1.6"><circle cx="12" cy="12" r="9"/><ellipse cx="12" cy="12" rx="4" ry="9"/><path d="M3 12h18M5 7h14M5 17h14"/></svg>
      <span>www.toluvek.org</span>
    </div>
  </footer>
</main>
</body>
</html>
```